Business card for my new company (Accounting firm)

I need a business card for my new business Corvane Advisory and Ledger SA. Our services are accounting, tax, audit and financial management. Our customers are small companies, start-ups and new companies. The final design has to show financial security, trust and growth. Please find our logo attached to the business card. Text for the business card: Corvane Advisory and Ledger SA Tomas da Varela Director and Founder Certified Accountant Tel. 022 418 27 35 tv@corvaneconseil.ch www.corvaneconseil.ch Rue des Vergers-Bleus 14 1201 Geneva
Target Market(s)
Our customers are small companies, start-ups and new companies.
Industry/Entity Type
Finance And Accounting
Contact Information for Business Card
Corvane Conseil et Registre SA
Tomas da Varela
Directeur et Fondateur
Expert-comptable diplômé
Tél. 022 418 27 35
tv@corvaneconseil.ch
www.corvaneconseil.ch
Rue des Vergers-Bleus 14
1201 Genève

```html
<!DOCTYPE html>
<html lang="fr">
<head>
<meta charset="utf-8">
<title>Corvane Conseil et Registre SA – Carte de visite</title>
<link rel="stylesheet" href="https://fonts.googleapis.com/css2?family=Roboto:wght@400;500;700&display=swap">
<style>
  :root {
    --page-bg: #d9dadb;
    --blue-light: #2fa3d8;
    --blue-mid: #2185bf;
    --blue-deep: #1b5f93;
    --navy-text: #1f5a92;
    --card-white: #f3f3f3;
    --ink: #333638;
    --ink-soft: #4a4d50;
    --strip-dark: #2f3032;
    --white: #ffffff;
  }
  * { box-sizing: border-box; margin: 0; padding: 0; }
  html, body {
    width: 1200px; height: 726px; overflow: hidden;
    background: var(--page-bg);
    font-family: "Roboto", Arial, sans-serif;
  }
  .sheet {
    position: relative; width: 1200px; height: 726px;
    display: flex; align-items: center; justify-content: center; gap: 50px;
  }
  .card {
    position: relative; width: 520px; height: 316px; overflow: hidden;
    box-shadow: 0 6px 18px rgba(0,0,0,0.18);
  }

  /* Front */
  .card-front {
    background: linear-gradient(160deg, var(--blue-light) 0%, var(--blue-mid) 50%, var(--blue-deep) 100%);
    color: var(--white);
    display: flex; flex-direction: column; align-items: center; justify-content: center;
  }
  .front-brand {
    display: flex; align-items: center; gap: 12px;
    font-weight: 700; font-size: 30px; letter-spacing: 0.5px;
  }
  .front-brand .brand-square {
    width: 22px; height: 22px; background: var(--white);
  }
  .front-website {
    margin-top: 46px; font-weight: 500; font-size: 15px; letter-spacing: 0.3px;
  }

  /* Back */
  .card-back { background: var(--card-white); }
  .back-brand {
    position: absolute; left: 34px; top: 142px; width: 210px;
    font-weight: 700; font-size: 26px; line-height: 1.15; color: var(--ink);
  }
  .back-brand .brand-square {
    display: block; width: 40px; height: 40px; margin-bottom: 14px;
    background: var(--blue-mid);
  }
  .contact {
    position: absolute; left: 270px; top: 34px; width: 240px;
  }
  .contact-name {
    font-weight: 700; font-size: 20px; color: var(--navy-text);
  }
  .contact-role {
    margin-top: 6px; font-size: 12px; line-height: 1.35; color: var(--ink-soft);
  }
  .contact-list { list-style: none; margin-top: 24px; }
  .contact-list li {
    display: flex; align-items: center; gap: 10px;
    font-size: 14px; color: var(--ink); line-height: 22px;
  }
  .contact-list svg { width: 13px; height: 13px; flex: none; fill: var(--ink-soft); }
  .address-band {
    position: absolute; right: 0; bottom: 20px; width: 310px; height: 50px;
    background: linear-gradient(90deg, var(--blue-deep), var(--blue-light));
    border-top-left-radius: 16px;
    display: flex; align-items: center; padding-left: 34px;
    color: var(--white); font-size: 14px; font-weight: 500;
  }
  .bottom-strip {
    position: absolute; left: 0; right: 0; bottom: 0; height: 20px;
    background: var(--strip-dark);
  }
</style>
</head>
<body>
<main class="sheet">
  <section class="card card-front" aria-label="Recto">
    <div class="front-brand"><span class="brand-square"></span>Corvane</div>
    <p class="front-website">www.corvaneconseil.ch</p>
  </section>

  <section class="card card-back" aria-label="Verso">
    <div class="back-brand"><span class="brand-square"></span>Corvane Conseil et Registre SA</div>
    <div class="contact">
      <h1 class="contact-name">Tomas da Varela</h1>
      <p class="contact-role">Directeur et Fondateur<br>Expert-comptable diplômé</p>
      <ul class="contact-list">
        <li><svg viewBox="0 0 16 16" aria-hidden="true"><path d="M3 1h3l1.5 4-2 1.5a9 9 0 0 0 4 4L11 8.5l4 1.5v3a2 2 0 0 1-2 2A12 12 0 0 1 1 3a2 2 0 0 1 2-2z"/></svg>022 418 27 35</li>
        <li><svg viewBox="0 0 16 16" aria-hidden="true"><path d="M1 3h14v10H1z M2 4l6 5 6-5" stroke="#f3f3f3" stroke-width="1"/></svg>tv@corvaneconseil.ch</li>
        <li><svg viewBox="0 0 16 16" aria-hidden="true"><circle cx="8" cy="8" r="7"/><path d="M1 8h14M8 1c-3 4-3 10 0 14M8 1c3 4 3 10 0 14" stroke="#f3f3f3" stroke-width="1" fill="none"/></svg>www.corvaneconseil.ch</li>
      </ul>
    </div>
    <div class="address-band">Rue des Vergers-Bleus 14 1201 Genève</div>
    <div class="bottom-strip"></div>
  </section>
</main>
</body>
</html>
```